Enterprise IT illustration needs a twist and uniquness

The attached Powerpoint shows four conceptual houses that consist of 5 / 6 building blocks. We will build a lot of content around this concept and want a design that looks crisp, in line with our brand colors guideline and with logo/ copyright embedded. Each building blocks should have unique color aligned with brand guideline so that content can easily aligned with the specific building block (by color). Look for a clean, modern design with a twist. Need the files also in formats where I can change text if needed at a later point.

```html
<!DOCTYPE html>
<html lang="en">
<head>
<meta charset="utf-8">
<title>Orvix – Building Blocks House</title>
<link rel="stylesheet" href="https://fonts.googleapis.com/css2?family=Poppins:wght@500;600&display=swap">
<style>
  :root {
    --page: #ffffff;
    --photo-light: #e4e4e2;
    --photo-mid: #cfcfcc;
    --photo-dark: #b9b7b3;
    --roof: #f5a800;
    --frame: #ffffff;
    --action: #4a5a9e;
    --alerting: #57d3e8;
    --learn: #e2a52d;
    --topology: #e8606e;
    --harvest: #e2cb2a;
    --dashboards: #4a4a4a;
    --ink: #222222;
    --brand: #f5a800;
  }
  * { box-sizing: border-box; margin: 0; padding: 0; }
  html, body { width: 977px; height: 1200px; overflow: hidden; background: var(--page); }
  body { position: relative; font-family: "Poppins", sans-serif; }

  .panel { position: absolute; left: 0; width: 977px; height: 550px; overflow: hidden; }
  .panel--top { top: 0; }
  .panel--bottom { top: 650px; }

  .scene-photo { position: absolute; inset: 0; }
  .panel--top .scene-photo { background: linear-gradient(100deg, var(--photo-dark) 0%, var(--photo-light) 35%, var(--photo-light) 65%, var(--photo-mid) 100%); }
  .panel--bottom .scene-photo { background: linear-gradient(100deg, var(--photo-mid) 0%, var(--photo-light) 40%, var(--photo-mid) 70%, var(--photo-dark) 100%); }

  .brand { position: absolute; left: 37px; top: 38px; display: flex; align-items: center; gap: 12px; }
  .brand__dot { width: 26px; height: 26px; border-radius: 50%; background: var(--brand); }
  .brand__name { font-size: 36px; font-weight: 500; color: var(--ink); line-height: 1; letter-spacing: 1px; }

  .house-shape { position: absolute; left: 0; top: 0; width: 977px; height: 550px; }

  .block {
    position: absolute; border: 7px solid var(--frame);
    display: flex; align-items: center; gap: 13px; padding-left: 9px;
    color: #fff; font-size: 23px; font-weight: 500; line-height: 1.1;
  }
  .block--alerting { background: var(--alerting); }
  .block--learn { background: var(--learn); }
  .block--topology { background: var(--topology); }
  .block--harvest { background: var(--harvest); }

  .label--action { position: absolute; display: flex; align-items: center; gap: 13px; color: #fff; font-size: 23px; font-weight: 500; }

  .num {
    flex: none; width: 35px; height: 35px; border-radius: 50%; background: #fff;
    display: flex; align-items: center; justify-content: center;
    font-size: 20px; font-weight: 600;
  }
  .num--action { color: var(--action); }
  .num--alerting { color: var(--alerting); }
  .num--learn { color: var(--learn); }
  .num--topology { color: var(--topology); }
  .num--harvest { color: var(--harvest); }

  .dashboards {
    position: absolute; border: 7px solid var(--frame); background: var(--dashboards);
    display: flex; flex-direction: column; align-items: center; padding-top: 8px; gap: 8px;
    color: #fff;
  }
  .dashboards__plus { width: 24px; height: 24px; }
  .dashboards__text { writing-mode: vertical-rl; font-size: 14px; font-weight: 500; letter-spacing: 1px; }
</style>
</head>
<body>

<section class="panel panel--top">
  <div class="scene-photo" role="img" aria-label="Soft-focus office photo of two smiling colleagues"></div>
  <div class="brand"><span class="brand__dot"></span><span class="brand__name">Orvix</span></div>
  <svg class="house-shape" viewBox="0 0 977 550" aria-hidden="true">
    <polyline points="233,174 543,65 740,177" fill="none" stroke="var(--roof)" stroke-width="15" stroke-linecap="round" stroke-linejoin="round"/>
    <polygon points="296,164 542,82 693,164 693,235 296,235" fill="var(--frame)"/>
    <polygon points="303,174 542,90 685,174 685,227 303,227" fill="var(--action)"/>
  </svg>
  <div class="label--action" style="left:312px; top:185px;"><span class="num num--action">5</span>Taking ACTION</div>
  <div class="block block--alerting" style="left:296px; top:241px; width:397px; height:66px;"><span class="num num--alerting">4</span>Business Relevant Alerting</div>
  <div class="block block--learn" style="left:296px; top:314px; width:190px; height:105px;"><span class="num num--learn">2</span>Learn &amp;<br>Correlate</div>
  <div class="block block--topology" style="left:492px; top:314px; width:201px; height:105px;"><span class="num num--topology">3</span>Topology<br>Discovery</div>
  <div class="block block--harvest" style="left:296px; top:424px; width:397px; height:68px;"><span class="num num--harvest">1</span>Quality DATA Harvesting</div>
</section>

<section class="panel panel--bottom">
  <div class="scene-photo" role="img" aria-label="Soft-focus office photo of colleagues in a meeting"></div>
  <div class="brand"><span class="brand__dot"></span><span class="brand__name">Orvix</span></div>
  <svg class="house-shape" viewBox="0 0 977 550" aria-hidden="true">
    <polyline points="200,172 550,63 775,176" fill="none" stroke="var(--roof)" stroke-width="15" stroke-linecap="round" stroke-linejoin="round"/>
    <polygon points="266,165 548,82 724,165 724,235 266,235" fill="var(--frame)"/>
    <polygon points="272,172 548,91 717,172 717,227 272,227" fill="var(--action)"/>
  </svg>
  <div class="label--action" style="left:281px; top:186px;"><span class="num num--action">5</span>Taking ACTION</div>
  <div class="block block--alerting" style="left:266px; top:241px; width:397px; height:66px;"><span class="num num--alerting">4</span>Business Relevant Alerting</div>
  <div class="dashboards" style="left:669px; top:241px; width:55px; height:175px;">
    <svg class="dashboards__plus" viewBox="0 0 24 24" aria-hidden="true">
      <circle cx="12" cy="12" r="12" fill="#fff"/>
      <path d="M12 6v12M6 12h12" stroke="var(--dashboards)" stroke-width="3"/>
    </svg>
    <span class="dashboards__text">DASHBOARDS</span>
  </div>
  <div class="block block--learn" style="left:266px; top:314px; width:190px; height:105px;"><span class="num num--learn">2</span>Learn &amp;<br>Correlate</div>
  <div class="block block--topology" style="left:461px; top:314px; width:202px; height:105px;"><span class="num num--topology">3</span>Topology<br>Discovery</div>
  <div class="block block--harvest" style="left:266px; top:424px; width:458px; height:68px;"><span class="num num--harvest">1</span>Quality DATA Harvesting</div>
</section>

</body>
</html>
```